Christmas Ballet Poster for La Marioneta

I urgently need a poster for the La Marioneta ballet, it needs to look magical and very similar to the reference attached. The title should be La Marioneta and the typography and look should be as similar as possible as the words Winter Lantern in the reference attached. Use a dancers photo just for reference, I will not use that photo as someone will be taking the picture of the principal dancer and we will be using that. It should look magical, upscale and pretty.
Requirements
Must have
- Title: La Marioneta
- Space for date, time and prices
- Space to add logo
- It must look as similar as the reference as possible, magical, elegant.
Should not have
- Any logo

```html
<!DOCTYPE html>
<html lang="en">
<head>
<meta charset="utf-8">
<title>La Marioneta – Ballet Poster</title>
<link rel="stylesheet" href="https://fonts.googleapis.com/css2?family=Almendra:wght@700&family=Fredoka:wght@500;600&display=swap">
<style>
  :root {
    --night: #07062e;
    --indigo: #1c1580;
    --violet: #3b2fc4;
    --glow: #fff3b0;
    --amber: #f2a64a;
    --spark: rgba(255, 214, 140, .95);
    --spark-fade: rgba(255, 170, 90, 0);
    --title-purple: #5b2ba6;
    --label-blue: #2a1fa0;
    --white: #ffffff;
    --logo-grey: #6b636f;
  }
  * { margin: 0; padding: 0; box-sizing: border-box; }
  html, body {
    width: 1200px; height: 800px; overflow: hidden;
    background: var(--night);
  }
  .poster {
    position: relative; width: 1200px; height: 800px; overflow: hidden;
    font-family: "Fredoka", sans-serif; color: var(--white);
  }
  .stage-scene {
    position: absolute; inset: 0;
    background:
      radial-gradient(ellipse 240px 130px at 612px 50px, var(--glow) 0%, rgba(242,166,74,.8) 35%, rgba(242,166,74,0) 100%),
      radial-gradient(ellipse 380px 560px at 612px 200px, rgba(210,120,200,.6) 0%, rgba(110,60,200,.4) 50%, rgba(59,47,196,0) 100%),
      radial-gradient(ellipse 190px 110px at 610px 700px, rgba(255,245,200,.95) 0%, rgba(242,166,74,.45) 40%, rgba(242,166,74,0) 100%),
      radial-gradient(ellipse 420px 160px at 560px 720px, rgba(200,90,200,.45) 0%, rgba(200,90,200,0) 100%),
      linear-gradient(90deg, var(--night) 0%, var(--indigo) 28%, var(--violet) 50%, var(--indigo) 74%, var(--night) 100%);
  }
  .sparkles {
    position: absolute; inset: 0;
    background:
      radial-gradient(circle 7px at 420px 290px, var(--spark), var(--spark-fade)),
      radial-gradient(circle 5px at 480px 250px, var(--spark), var(--spark-fade)),
      radial-gradient(circle 6px at 520px 330px, var(--spark), var(--spark-fade)),
      radial-gradient(circle 8px at 700px 230px, var(--spark), var(--spark-fade)),
      radial-gradient(circle 5px at 760px 300px, var(--spark), var(--spark-fade)),
      radial-gradient(circle 6px at 820px 260px, var(--spark), var(--spark-fade)),
      radial-gradient(circle 9px at 898px 355px, var(--spark), var(--spark-fade)),
      radial-gradient(circle 5px at 950px 420px, var(--spark), var(--spark-fade)),
      radial-gradient(circle 7px at 925px 550px, var(--spark), var(--spark-fade)),
      radial-gradient(circle 10px at 628px 545px, var(--spark), var(--spark-fade)),
      radial-gradient(circle 6px at 560px 600px, var(--spark), var(--spark-fade)),
      radial-gradient(circle 5px at 520px 640px, var(--spark), var(--spark-fade)),
      radial-gradient(circle 7px at 470px 690px, var(--spark), var(--spark-fade)),
      radial-gradient(circle 5px at 700px 620px, var(--spark), var(--spark-fade)),
      radial-gradient(circle 6px at 745px 660px, var(--spark), var(--spark-fade)),
      radial-gradient(circle 4px at 560px 740px, var(--spark), var(--spark-fade)),
      radial-gradient(circle 5px at 380px 520px, var(--spark), var(--spark-fade)),
      radial-gradient(circle 4px at 330px 440px, var(--spark), var(--spark-fade)),
      radial-gradient(circle 6px at 440px 420px, var(--spark), var(--spark-fade)),
      radial-gradient(circle 4px at 990px 240px, var(--spark), var(--spark-fade)),
      radial-gradient(circle 4px at 860px 470px, var(--spark), var(--spark-fade)),
      radial-gradient(circle 3px at 250px 560px, var(--white), rgba(255,255,255,0)),
      radial-gradient(circle 3px at 140px 240px, var(--white), rgba(255,255,255,0)),
      radial-gradient(circle 3px at 230px 180px, var(--white), rgba(255,255,255,0)),
      radial-gradient(circle 3px at 1080px 200px, var(--white), rgba(255,255,255,0)),
      radial-gradient(circle 3px at 1010px 720px, var(--white), rgba(255,255,255,0)),
      radial-gradient(circle 3px at 60px 600px, var(--white), rgba(255,255,255,0)),
      radial-gradient(circle 3px at 1150px 480px, var(--white), rgba(255,255,255,0));
  }
  .dancers-photo {
    position: absolute; left: 270px; top: 230px; width: 620px; height: 570px;
    border-radius: 48% 48% 0 0 / 40% 40% 0 0;
    background:
      radial-gradient(ellipse 150px 230px at 35% 50%, rgba(170,50,150,.55) 0%, rgba(170,50,150,0) 100%),
      radial-gradient(ellipse 150px 230px at 70% 60%, rgba(150,180,255,.6) 0%, rgba(150,180,255,0) 100%),
      radial-gradient(ellipse at 50% 55%, rgba(170,160,255,.35) 0%, rgba(90,70,200,.2) 55%, rgba(60,40,180,0) 80%);
  }
  .title {
    position: absolute; left: 0; right: 0; top: 46px;
    text-align: center; padding-left: 58px;
    font-family: "Almendra", serif; font-weight: 700; font-size: 146px; line-height: 1;
    letter-spacing: -2px;
    color: var(--title-purple);
    -webkit-text-stroke: 4px var(--white); paint-order: stroke fill;
  }
  .label {
    font-family: "Almendra", serif; font-weight: 700; line-height: 1;
    color: var(--label-blue);
    -webkit-text-stroke: 3px var(--white); paint-order: stroke fill;
  }
  .value { font-weight: 600; line-height: 1; letter-spacing: 1px; }
  .event-date { position: absolute; left: 66px; top: 290px; }
  .event-date .label { font-size: 80px; }
  .event-date .value { font-size: 55px; margin-top: 34px; }
  .event-time { position: absolute; right: 52px; top: 306px; text-align: right; }
  .event-time .label { font-size: 66px; }
  .event-time .value { font-size: 55px; margin-top: 30px; }
  .prices { position: absolute; right: 48px; top: 524px; width: 250px; }
  .prices .label { font-size: 56px; text-align: right; margin-bottom: 10px; letter-spacing: -1px; }
  .price-list { list-style: none; }
  .price-row {
    display: flex; justify-content: space-between; align-items: center;
    height: 44px; margin-bottom: 6px; padding: 0 12px 0 14px;
    border: 2px solid var(--white); border-radius: 22px;
    font-weight: 500; font-size: 29px;
  }
  .logo-space {
    position: absolute; left: 63px; top: 668px; width: 263px; height: 139px;
    border-radius: 26px; background: var(--logo-grey);
    display: flex; align-items: center; justify-content: center;
    font-weight: 600; font-size: 46px; letter-spacing: 1px;
  }
</style>
</head>
<body>
<main class="poster">
  <div class="stage-scene" role="img" aria-label="Glowing theatre stage with golden light in deep blue and violet"></div>
  <div class="dancers-photo" role="img" aria-label="Photo of two ballet dancers: a man in a red jacket and a ballerina in a pale blue tutu"></div>
  <div class="sparkles" role="img" aria-label="Floating golden sparkles"></div>

  <h1 class="title">La Marioneta</h1>

  <section class="event-date">
    <div class="label">Date</div>
    <div class="value">01.12.2018</div>
  </section>

  <section class="event-time">
    <div class="label">Time</div>
    <div class="value">6.00 PM</div>
  </section>

  <section class="prices">
    <div class="label">PRICES</div>
    <ul class="price-list">
      <li class="price-row"><span>ADULT</span><span>50 $</span></li>
      <li class="price-row"><span>COUPLE</span><span>80 $</span></li>
      <li class="price-row"><span>CHILDREN</span><span>20 $</span></li>
    </ul>
  </section>

  <div class="logo-space">LOGO</div>
</main>
</body>
</html>
```